Re-design / re-work of existing website

Need to re-design a website so it's easy for me as a user to update/add pictures and change descriptions.

If possible, would there be a way to display LodgeVista calendars? We have 3 cottages and it would be ideal to have each cottage with pics on one page along with a readonly version of the LodgeVista calendar plugin (if such a thing exists) so that visitors to the site can see what is available and what is not.

Existing site: http://tarnwoodlets.net

```html
<!DOCTYPE html>
<html lang="en">
<head>
<meta charset="utf-8">
<title>Tarnwood Cottages</title>
<link href="https://fonts.googleapis.com/css2?family=Josefin+Sans:wght@400;600;700&family=Great+Vibes&family=Kumbh+Sans:wght@400;500;600&display=swap" rel="stylesheet">
<style>
:root{
  --taupe:#978d85;
  --taupe-soft:#9a9088;
  --ink:#121416;
  --white:#ffffff;
  --gold:#c4a163;
  --badge:#e2c11c;
  --booked:#3b9a45;
  --footer-text:#e6e1da;
  --map-land:#c9e3c6;
  --map-water:#a9d0dc;
}
*{box-sizing:border-box;margin:0;padding:0}
html,body{width:1200px;height:3706px;overflow:hidden}
body{font-family:"Kumbh Sans",sans-serif;background:var(--taupe);color:var(--ink);position:relative}
.abs{position:absolute}
.script{font-family:"Great Vibes",cursive;font-weight:400}
.photo{position:absolute;display:block}

/* background texture areas */
.texture{position:absolute;left:0;width:1200px;background:radial-gradient(ellipse at 30% 40%,var(--taupe-soft),var(--taupe) 70%)}

/* hero */
.hero{position:absolute;left:0;top:0;width:1200px;height:531px;background:linear-gradient(135deg,#6b4a2e 0%,#8a6a4c 30%,#b9a795 55%,#7a4a35 80%,#4a3224 100%)}
.hero-shade{position:absolute;left:0;top:0;width:1200px;height:531px;background:rgba(0,0,0,.32)}
.logo{position:absolute;left:138px;top:38px;color:var(--white);font-size:17px;font-weight:500;display:flex;align-items:center;gap:8px}
.logo i{width:10px;height:10px;border:1.5px solid var(--white);display:block}
.nav{position:absolute;top:39px;left:0;width:1200px;font-size:11.5px;color:var(--white)}
.nav span{position:absolute;white-space:nowrap}
.nav .active{color:var(--gold)}
.nav .phone{color:var(--gold);display:flex;gap:5px;align-items:center}
.btn-outline{position:absolute;border:1.4px solid var(--white);border-radius:20px;color:var(--white);font-size:11.5px;font-weight:600;display:flex;align-items:center;justify-content:center}
.hero-title{position:absolute;left:0;width:1200px;text-align:center;color:var(--white);font-family:"Josefin Sans",sans-serif;font-weight:700;line-height:1}
.hero-title .script{font-size:108px}
.weather{position:absolute;left:1000px;top:479px;width:125px;height:104px;background:var(--white);border-radius:4px;font-size:8px;color:#333;text-align:center;overflow:hidden}
.weather .head{height:14px;background:var(--badge);display:flex;align-items:center;justify-content:center}
.weather .head i{width:8px;height:8px;background:#fff;border-radius:50%;display:block}
.weather .place{font-size:9px;margin-top:3px;border-bottom:1px solid #ddd;padding-bottom:3px}
.weather .cols{display:flex;margin-top:3px}
.weather .cols div{flex:1;line-height:1.6}
.weather .cols div+div{border-left:1px solid #ddd}
.weather b{font-size:11px}

/* section headings */
.sec-title{position:absolute;left:0;width:1200px;text-align:center;color:var(--white);font-family:"Josefin Sans",sans-serif;font-weight:400;font-size:42px;line-height:1}
.sec-title .script{font-size:58px}

/* cottages */
.badge{position:absolute;font-size:9px;padding:3px 14px;color:var(--white);border-radius:2px}
.badge.available{background:var(--badge)}
.badge.booked{background:var(--booked)}
.c-name{position:absolute;width:260px;text-align:center;font-family:"Josefin Sans",sans-serif;font-weight:400;font-size:19px;color:var(--ink)}
.c-name .script{font-size:34px}
.c-specs{position:absolute;width:260px;display:flex;justify-content:center;gap:44px;font-size:11px;color:var(--white)}
.c-specs div{display:flex;flex-direction:column;align-items:center;gap:4px}
.c-desc{position:absolute;width:260px;text-align:center;font-size:12px;color:var(--white);line-height:1.25}
.btn-dark{position:absolute;background:var(--ink);color:var(--white);border-radius:20px;font-size:11.5px;font-weight:600;display:flex;align-items:center;justify-content:center}
.btn-gold{position:absolute;background:var(--gold);color:var(--white);border-radius:20px;font-size:11.5px;font-weight:600;display:flex;align-items:center;justify-content:center}

/* welcome */
.welcome-box{position:absolute;left:331px;top:1506px;width:669px;height:418px;background:var(--ink);color:var(--white)}
.welcome-box h2{position:absolute;left:75px;top:64px;font-family:"Josefin Sans",sans-serif;font-weight:400;font-size:34px;line-height:1}
.welcome-box .brand{position:absolute;left:75px;top:100px;font-size:62px;line-height:1;white-space:nowrap}
.welcome-box p{position:absolute;left:75px;top:198px;width:540px;font-size:10.5px;line-height:22.5px}

/* explore */
.tile-label{position:absolute;background:rgba(90,82,76,.75);color:var(--white);font-size:13px;padding:6px 12px;white-space:nowrap}

/* footer */
.footer{position:absolute;left:0;top:3269px;width:1200px;height:437px;background:var(--ink);color:var(--footer-text)}
.f-logo{position:absolute;left:75px;top:110px;font-size:22px;font-weight:500;color:var(--white);display:flex;align-items:center;gap:10px}
.f-logo i{width:12px;height:12px;border:1.5px solid var(--white);display:block}
.social{position:absolute;width:32px;height:32px;border-radius:50%;background:#6d6862}
.social.on{background:var(--gold)}
.f-head{position:absolute;color:var(--white);font-family:"Josefin Sans",sans-serif;font-size:15px}
.f-head .script{font-size:26px}
.f-item{position:absolute;font-size:11px;color:var(--footer-text);display:flex;gap:10px;align-items:flex-start;line-height:1.4}
.f-item svg{flex:none;margin-top:1px}
.f-link{position:absolute;left:587px;font-size:11px}
.divider{position:absolute;left:75px;top:329px;width:719px;height:1px;background:#2e3134}
.copy{position:absolute;left:75px;top:375px;font-size:10px;color:var(--white)}
.copy span{color:var(--gold)}
.map{position:absolute;left:794px;top:3219px;width:406px;height:437px;background:linear-gradient(160deg,var(--map-land) 0%,var(--map-land) 45%,var(--map-water) 100%)}
</style>
</head>
<body>

<div class="texture" style="top:531px;height:1132px" role="img" aria-label="Faint topographic contour pattern"></div>
<div class="texture" style="top:2130px;height:1139px" role="img" aria-label="Faint topographic contour pattern"></div>

<!-- HERO -->
<section class="hero" role="img" aria-label="Bright cottage interior with wood panelling, leather sofas and kitchen"></section>
<div class="hero-shade"></div>
<div class="logo"><i></i>Tarnwood Cottages</div>
<nav class="nav">
  <span class="active" style="left:466px">Home</span>
  <span style="left:529px">Our Cottages</span>
  <span style="left:630px">Adventures</span>
  <span style="left:720px">Getting Here</span>
  <span class="phone" style="left:818px">
    <svg width="10" height="10" viewBox="0 0 24 24"><path d="M6.6 10.8a15 15 0 0 0 6.6 6.6l2.2-2.2c.3-.3.7-.4 1-.2 1.1.4 2.3.6 3.6.6.6 0 1 .4 1 1V20c0 .6-.4 1-1 1A17 17 0 0 1 3 4c0-.6.4-1 1-1h3.5c.6 0 1 .4 1 1 0 1.3.2 2.5.6 3.6.1.3 0 .7-.2 1z" fill="#c4a163"/></svg>
    +1 555 214 0387</span>
</nav>
<div class="btn-outline" style="left:951px;top:28px;width:112px;height:37px">Contact Us</div>

<div class="hero-title" style="top:170px;font-size:58px"><span class="script">Come</span> and <span class="script">Enjoy</span> life</div>
<div class="hero-title" style="top:302px;font-size:58px">on the Water!</div>
<div class="btn-outline" style="left:544px;top:383px;width:112px;height:35px">Contact Us</div>
<svg class="abs" style="left:588px;top:482px" width="16" height="20" viewBox="0 0 16 20"><path d="M8 1v17M2 12l6 6 6-6" stroke="#fff" stroke-width="1.6" fill="none"/></svg>

<div class="weather">
  <div class="head"><i></i></div>
  <div class="place">Lakeview, ON &#9662;</div>
  <div class="cols">
    <div>Current<br><b>11°C</b><br>Overcast</div>
    <div>Tue Morn<br><b>11°C</b><br>Cloudy</div>
  </div>
</div>

<!-- DISCOVER -->
<h2 class="sec-title" style="top:630px"><span class="script">Discover</span> the Magic of the</h2>
<h2 class="sec-title" style="top:690px">Tarnwood <span class="script">Cottages</span></h2>

<!-- Aspen -->
<div class="photo" style="left:75px;top:865px;width:256px;height:280px;background:linear-gradient(160deg,#d8d2c6,#a8764a 50%,#6e4a30)" role="img" aria-label="Aspen cottage living room with pine walls"></div>
<div class="badge available" style="left:172px;top:1138px">Available</div>
<div class="c-name" style="left:73px;top:1172px"><span class="script">The</span> Aspen</div>
<div class="c-specs" style="left:73px;top:1234px">
  <div><svg width="20" height="16" viewBox="0 0 20 16"><path d="M2 14V4M2 10h16v4M4 8V6h5v2M11 8V6h5v2" stroke="#fff" fill="none" stroke-width="1.2"/></svg>3 Bedroom</div>
  <div><svg width="20" height="16" viewBox="0 0 20 16"><path d="M2 8h16v2a4 4 0 0 1-4 4H6a4 4 0 0 1-4-4zM5 8V3a2 2 0 0 1 4 0" stroke="#fff" fill="none" stroke-width="1.2"/></svg>1 Bathroom</div>
</div>
<div class="c-desc" style="left:73px;top:1288px">With large kitchen and<br>living space</div>
<div class="btn-dark" style="left:141px;top:1335px;width:124px;height:38px">Check Availability</div>

<!-- Birch -->
<div class="photo" style="left:406px;top:811px;width:387px;height:388px;background:linear-gradient(160deg,#e9e6e0,#b79a76 45%,#8a5a3a 75%,#5e3a28)" role="img" aria-label="Birch cottage open kitchen and living area"></div>
<div class="badge booked" style="left:572px;top:1192px">Booked</div>
<div class="c-name" style="left:470px;top:1225px"><span class="script">The</span> Birch</div>
<div class="c-specs" style="left:470px;top:1287px">
  <div><svg width="20" height="16" viewBox="0 0 20 16"><path d="M2 14V4M2 10h16v4M4 8V6h5v2M11 8V6h5v2" stroke="#fff" fill="none" stroke-width="1.2"/></svg>3 Bedroom</div>
  <div><svg width="20" height="16" viewBox="0 0 20 16"><path d="M2 8h16v2a4 4 0 0 1-4 4H6a4 4 0 0 1-4-4zM5 8V3a2 2 0 0 1 4 0" stroke="#fff" fill="none" stroke-width="1.2"/></svg>2 Bathroom</div>
</div>
<div class="c-desc" style="left:470px;top:1341px">With large kitchen and<br>living space</div>
<div class="btn-gold" style="left:538px;top:1388px;width:124px;height:38px">Explore More</div>

<!-- Cedar -->
<div class="photo" style="left:869px;top:865px;width:256px;height:280px;background:linear-gradient(160deg,#e6e4df,#8e9aa0 45%,#a7764c 75%,#2f6fa5)" role="img" aria-label="Cedar cottage dining room with blue armchair"></div>
<div class="badge available" style="left:966px;top:1138px">Available</div>
<div class="c-name" style="left:867px;top:1172px"><span class="script">The</span> Cedar</div>
<div class="c-specs" style="left:867px;top:1234px">
  <div><svg width="20" height="16" viewBox="0 0 20 16"><path d="M2 14V4M2 10h16v4M4 8V6h5v2M11 8V6h5v2" stroke="#fff" fill="none" stroke-width="1.2"/></svg>3 Bedroom</div>
  <div><svg width="20" height="16" viewBox="0 0 20 16"><path d="M2 8h16v2a4 4 0 0 1-4 4H6a4 4 0 0 1-4-4zM5 8V3a2 2 0 0 1 4 0" stroke="#fff" fill="none" stroke-width="1.2"/></svg>1 Bathroom</div>
</div>
<div class="c-desc" style="left:867px;top:1288px">With large kitchen and<br>living space</div>
<div class="btn-dark" style="left:935px;top:1335px;width:124px;height:38px">Check Availability</div>

<!-- WELCOME -->
<div class="photo" style="left:0;top:1663px;width:1200px;height:467px;background:linear-gradient(90deg,#a9a6a2 0%,#c49a66 20%,#9aa4aa 45%,#8b6440 60%,#2e6aa0 78%,#d8dde0 90%,#b7c4cc 100%)" role="img" aria-label="Cottage dining room with wooden table and view of the lake"></div>
<div class="welcome-box">
  <h2>Welcome to</h2>
  <div class="brand script">Tarnwood Cottages</div>
  <p>This quaint 3 cottage oasis is situated in a woodland setting yet right off Tarnwood Road, on the shores of beautiful Heron Lake. Our cottages are a little over 3 hours' drive from Toronto, and about an hour's drive from Sudbury. Heron lake is a calm and quiet lake with little water traffic, which makes it a very safe destination for kids, and all kinds of water sports and activities.</p>
</div>
<div class="btn-gold" style="left:406px;top:1813px;width:125px;height:36px">Discover More</div>

<!-- EXPLORE -->
<h2 class="sec-title" style="top:2208px"><span class="script">Things</span> to Explore</h2>
<h2 class="sec-title" style="top:2268px"><span class="script">Near</span> Tarnwood <span class="script">Cottages</span></h2>

<div class="photo" style="left:138px;top:2394px;width:268px;height:193px;background:linear-gradient(170deg,#2b2f5a,#5a4d78 50%,#3a2a22)" role="img" aria-label="Visitor centre building lit at dusk"></div>
<div class="tile-label" style="left:138px;top:2527px">Pinecrest Visitor Centre</div>

<div class="photo" style="left:432px;top:2391px;width:336px;height:415px;background:linear-gradient(180deg,#6f8c6a,#3f5a36 35%,#b5bcc0 60%,#5d6a70)" role="img" aria-label="Rapids rushing through forested rocks"></div>
<div class="tile-label" style="left:432px;top:2423px">Whitewater Falls</div>

<div class="photo" style="left:794px;top:2394px;width:268px;height:193px;background:linear-gradient(180deg,#c9ccc8,#7a6a5c 45%,#5a5650)" role="img" aria-label="Trading post store with parking lot"></div>
<div class="tile-label" style="left:794px;top:2475px">Riverbend Trading Post</div>

<div class="photo" style="left:75px;top:2613px;width:331px;height:193px;background:linear-gradient(180deg,#6c7590,#8a90a0 40%,#3f4a3a 70%,#5a5e60)" role="img" aria-label="Calm lake with rocky shore and pine trees"></div>
<div class="tile-label" style="left:75px;top:2738px">Lakeview Provincial Park</div>

<div class="photo" style="left:794px;top:2613px;width:331px;height:193px;background:linear-gradient(180deg,#b7b4b8,#d9b489 45%,#5c5450 75%,#8a3a36)" role="img" aria-label="Red chairs on rocks at sunset by the water"></div>
<div class="tile-label" style="left:794px;top:2636px">Stone Point Park</div>

<div class="photo" style="left:200px;top:2832px;width:800px;height:310px;background:linear-gradient(180deg,#8a8f92,#6b7074 40%,#5a5550 70%,#4a5a40)" role="img" aria-label="Marina dock with boats and canoes"></div>
<div class="tile-label" style="left:200px;top:2972px">Tarnwood Marina</div>

<!-- FOOTER -->
<footer class="footer">
  <div class="f-logo"><i></i>Tarnwood Cottages</div>
  <div class="social" style="left:112px;top:230px"></div>
  <div class="social on" style="left:149px;top:230px"></div>
  <div class="social" style="left:187px;top:230px"></div>
  <div class="social" style="left:224px;top:230px"></div>

  <div class="f-head" style="left:331px;top:72px"><span class="script">Contact</span> us</div>
  <div class="f-item" style="left:331px;top:122px">
    <svg width="11" height="11" viewBox="0 0 24 24"><path d="M6.6 10.8a15 15 0 0 0 6.6 6.6l2.2-2.2c.3-.3.7-.4 1-.2 1.1.4 2.3.6 3.6.6.6 0 1 .4 1 1V20c0 .6-.4 1-1 1A17 17 0 0 1 3 4c0-.6.4-1 1-1h3.5c.6 0 1 .4 1 1 0 1.3.2 2.5.6 3.6.1.3 0 .7-.2 1z" fill="#c4a163"/></svg>
    <span style="font-size:12px">+1 555 214 0387</span></div>
  <div class="f-item" style="left:331px;top:152px">
    <svg width="11" height="11" viewBox="0 0 24 24"><rect x="2" y="5" width="20" height="14" rx="2" fill="#c4a163"/><path d="M2 6l10 7 10-7" stroke="#121416" stroke-width="1.6" fill="none"/></svg>
    <span style="text-decoration:underline">support@tarnwoodlets.net</span></div>
  <div class="f-item" style="left:331px;top:180px">
    <svg width="11" height="12" viewBox="0 0 24 26"><path d="M12 1a8 8 0 0 0-8 8c0 6 8 15 8 15s8-9 8-15a8 8 0 0 0-8-8zm0 11a3 3 0 1 1 0-6 3 3 0 0 1 0 6z" fill="#c4a163"/></svg>
    <span>418 Tarnwood Road, Lakeview<br>K0L 2B0</span></div>
  <div class="btn-outline" style="left:331px;top:229px;width:124px;height:35px;border-color:#c4a163;color:#c4a163;border-width:1px">Get Directions</div>

  <div class="f-head" style="left:587px;top:75px"><span class="script">Quick</span> links</div>
  <div class="f-link" style="top:125px">Home</div>
  <div class="f-link" style="top:150px">Our Cottages</div>
  <div class="f-link" style="top:175px">Adventures</div>
  <div class="f-link" style="top:200px">Getting Here</div>
  <div class="f-link" style="top:225px">Policies</div>
  <div class="f-link" style="top:250px">Contact Us</div>

  <div class="divider"></div>
  <div class="copy">© 2023 <span>Tarnwood Cottages</span>. All Rights Reserved</div>
</footer>
<div class="map" role="img" aria-label="Map of the area around the cottages"></div>

</body>
</html>
```